Retractable Banner Design Featuring Key Product for Beauty Trade Show

We're a beauty/nail supply company that specializes in products used in professional nail salons. The key product for this design is Disposable Latex Gloves.
We will be exhibiting in a trade show this summer and are looking for a free-standing Retractable Banner Design that will be displayed at the front of our booth. The goal of the banner will be to display key products that are high in demand with our customers. The banner will be used to attract attention and highlight key selling points of these popular products. We would like the banner to be focused on the product title, image and key points, with a beauty/model/pattern background to create a professional appearance.
Target Market(s)
Nail Salons
Industry/Entity Type
Nail & Beauty Industry

```html
<!DOCTYPE html>
<html lang="en">
<head>
<meta charset="utf-8">
<title>Disposable Latex Gloves – Retractable Banner</title>
<link rel="stylesheet" href="https://fonts.googleapis.com/css2?family=Josefin+Sans:wght@400;700&family=Lato:wght@400;900&display=swap">
<style>
  :root {
    --stage: #eef2f8;
    --purple-deep: #5a2472;
    --purple-mid: #7a3f9c;
    --purple-dark: #3f1450;
    --coral: #f0625a;
    --pink: #f08fc0;
    --white: #ffffff;
    --icon-coral: #f26a6a;
    --strip-edge: #4a1a35;
  }
  * { box-sizing: border-box; margin: 0; padding: 0; }
  html, body { width: 1200px; height: 1172px; overflow: hidden; }
  body {
    background: var(--stage);
    position: relative;
    font-family: "Lato", sans-serif;
  }
  .banner {
    position: absolute;
    left: 364px; top: 32px;
    width: 471px; height: 1108px;
    overflow: hidden;
    background: linear-gradient(180deg,
      var(--pink) 9%, #f2789a 22%, var(--coral) 33%, #c1558a 50%,
      var(--purple-mid) 66%, #6d338f 82%, var(--purple-deep) 100%);
  }
  .banner-header {
    position: absolute; left: 0; top: 0;
    width: 371px; height: 97px;
    background: linear-gradient(90deg, var(--purple-deep) 0%, #63287c 65%, #7b4aa6 100%);
    padding: 22px 0 0 26px;
    color: var(--white);
    font-family: "Josefin Sans", sans-serif;
    font-weight: 700;
    font-size: 15px;
    line-height: 19px;
    letter-spacing: 0.22em;
  }
  .product-boxes {
    position: absolute; left: 37px; top: 84px;
    width: 294px; height: 193px;
    background: linear-gradient(135deg, #f7f3ef 0%, #f2a36a 55%, #e8662a 100%);
    border-radius: 3px;
  }
  .gloves-photo {
    position: absolute; left: 9px; top: 320px;
    width: 362px; height: 474px;
    background: linear-gradient(160deg, rgba(250,245,245,0.85) 0%, rgba(240,232,232,0.75) 50%, rgba(245,205,180,0.55) 100%);
    border-radius: 40px 10px 0 60px;
  }
  .title-strip {
    position: absolute; right: 0; top: 0;
    width: 100px; height: 1108px;
    background: linear-gradient(180deg, var(--coral) 0%, #b85580 25%, var(--purple-mid) 45%, #6a2f8c 70%, var(--purple-deep) 100%);
    border-left: 14px solid var(--strip-edge);
    display: flex; align-items: center; justify-content: center;
  }
  .title-strip h1 {
    writing-mode: vertical-rl;
    color: var(--white);
    font-family: "Josefin Sans", sans-serif;
    font-weight: 700;
    font-size: 44px;
    letter-spacing: 0.34em;
    line-height: 1;
    white-space: nowrap;
    margin-left: -4px;
  }
  .features {
    position: absolute; left: 26px; top: 764px;
    list-style: none;
  }
  .feature {
    display: flex; align-items: center;
    height: 52px; margin-bottom: 17px;
    color: var(--white);
  }
  .feature-icon {
    width: 52px; height: 52px; flex: none;
    border-radius: 50%;
    background: radial-gradient(circle at 40% 35%, #f68a84, var(--icon-coral));
    display: flex; align-items: center; justify-content: center;
    margin-right: 20px;
  }
  .feature-text { font-size: 17px; line-height: 22px; }
  .feature-text strong { font-weight: 900; font-size: 18px; display: block; letter-spacing: 0.01em; }
  .feature-text span { font-weight: 400; display: block; }
</style>
</head>
<body>
  <section class="banner">
    <header class="banner-header">
      <p>(1,000 PCS/CASE)</p>
      <p>(84 CASES PER PALLET)</p>
    </header>

    <div class="product-boxes" role="img" aria-label="Product photo of two orange and white latex glove boxes, size small"></div>
    <div class="gloves-photo" role="img" aria-label="Photo of hands pulling on white disposable latex gloves"></div>

    <div class="title-strip">
      <h1>DISPOSABLE LATEX GLOVES</h1>
    </div>

    <ul class="features">
      <li class="feature">
        <div class="feature-icon">
          <svg width="28" height="28" viewBox="0 0 28 28" fill="none" stroke="#fff" stroke-width="1.6" stroke-linecap="round" stroke-linejoin="round">
            <path d="M4 20h8l8-4M4 24h10l10-6"/><path d="M10 16l6-10 6 10z"/><circle cx="15" cy="12" r="0.8"/><circle cx="18" cy="13" r="0.8"/>
          </svg>
        </div>
        <div class="feature-text"><strong>100% Powder-Free</strong><span>– no residue or irritants</span></div>
      </li>
      <li class="feature">
        <div class="feature-icon">
          <svg width="28" height="28" viewBox="0 0 28 28" fill="none" stroke="#fff" stroke-width="1.6" stroke-linecap="round" stroke-linejoin="round">
            <path d="M8 25V14L6 9M8 14V5M12 13V3M16 13V4M20 14V7M8 25h12V14l3-4"/>
            <circle cx="12" cy="18" r="0.8"/><circle cx="16" cy="18" r="0.8"/><circle cx="14" cy="21" r="0.8"/>
          </svg>
        </div>
        <div class="feature-text"><strong>Premium Textured Grip</strong><span>for Superior Grip</span></div>
      </li>
      <li class="feature">
        <div class="feature-icon">
          <svg width="30" height="28" viewBox="0 0 30 28" fill="none" stroke="#fff" stroke-width="1.8" stroke-linecap="round" stroke-linejoin="round">
            <path d="M9 8l-6 6 6 6M21 8l6 6-6 6M9 14h12"/><path d="M12 11l-3 3 3 3M18 11l3 3-3 3"/>
          </svg>
        </div>
        <div class="feature-text"><strong>6.2g Latex</strong><span>– Super Heavy Duty</span></div>
      </li>
      <li class="feature">
        <div class="feature-icon">
          <svg width="28" height="28" viewBox="0 0 28 28" fill="none" stroke="#fff" stroke-width="1.6" stroke-linecap="round" stroke-linejoin="round">
            <path d="M10 25V10a4 4 0 0 1 8 0v15"/><path d="M11.5 11a2.5 2.5 0 0 1 5 0v3h-5z"/><path d="M4 6l1 1M23 6l1 1M3 14h2M23 14h2"/>
          </svg>
        </div>
        <div class="feature-text"><span>Designed for</span><strong>Professional Salons!</strong></div>
      </li>
    </ul>
  </section>
</body>
</html>
```